Health Coach needs a Business Card Design

Need a really modern feminine business card design for a health and lifestyle coach. Needs to use geometric shapes, muted grey/blue/green pastels and black and white - see mood board attached and logo. The client likes black and white, modern, san serif with the use of lines and possibly a shadow leaf as in the mood board. Possibly put the tag line on the back or an icon of the logo. Logo is also attached. An icon of the logo would be great too.

Target Market(s)

Women (some men) aged 30 to 50.

Industry/Entity Type

Business

Contact Information for Business Card

Marla Teveny
e-mail: hello@marlatwell.example
website: marlatwell.example
Phone: +610497258316

The tag line is "Calm strength, every day"

Font styles to use
Sans Serif

Colors
ecf7fb
cfeae6
000000
ffffff
f5f5f5

Requirements
Must have
• Black and white, logo, tag line and details
Nice to have
• Would be nice to incorporate the shadow palm.fern leaves as in the mood board and or geometric lines/shapes - see mood board. Could be either standard rectangle or would be happy with square too.
Should not have
• Flowers or decorations

```html
<!DOCTYPE html>
<html lang="en">
<head>
<meta charset="utf-8">
<title>Marla T — Business Card</title>
<link rel="stylesheet" href="https://fonts.googleapis.com/css2?family=Jost:wght@300;400&display=swap">
<style>
  :root {
    --stage: #161616;
    --card: #ecf7fb;
    --ink: #000000;
    --edge: #d9e4e8;
  }
  html, body {
    margin: 0;
    padding: 0;
    overflow: hidden;
  }
  body {
    width: 1200px;
    height: 741px;
    background: var(--stage);
    position: relative;
    font-family: "Jost", "Helvetica Neue", Arial, sans-serif;
    color: var(--ink);
  }
  .card {
    position: absolute;
    top: 228px;
    width: 495px;
    height: 283px;
    background: var(--card);
    border: 1px solid var(--edge);
    box-sizing: border-box;
    text-align: center;
  }
  .card--front { left: 100px; }
  .card--back { left: 606px; }

  .brand-name {
    position: absolute;
    left: 0;
    right: 0;
    font-weight: 300;
    font-size: 30px;
    letter-spacing: 2px;
    line-height: 1;
    margin: 0;
  }
  .tagline {
    position: absolute;
    left: 0;
    right: 0;
    font-weight: 400;
    font-size: 10.5px;
    letter-spacing: 3.2px;
    text-transform: uppercase;
    line-height: 1;
    margin: 0;
  }
  .card--front .brand-name { top: 117px; padding-left: 30px; }
  .card--front .tagline { top: 161px; padding-left: 46px; }

  .card--back .brand-name { top: 62px; padding-left: 20px; }
  .card--back .tagline { top: 106px; }

  .holder-name {
    position: absolute;
    top: 164px;
    left: 0;
    right: 0;
    margin: 0;
    font-weight: 400;
    font-size: 17px;
    letter-spacing: 1.4px;
    text-transform: uppercase;
    line-height: 1;
  }
  .contact {
    position: absolute;
    top: 195px;
    left: 0;
    right: 0;
    margin: 0;
    font-weight: 400;
    font-size: 13px;
    line-height: 17px;
  }
  .contact span { display: block; }
</style>
</head>
<body>
  <section class="card card--front">
    <h1 class="brand-name">Marla T</h1>
    <p class="tagline">Calm strength, every day</p>
  </section>

  <section class="card card--back">
    <h2 class="brand-name">Marla T</h2>
    <p class="tagline">Calm strength, every day</p>
    <p class="holder-name">Marla Teveny</p>
    <p class="contact">
      <span>p: +610497258316 | e: hello@marlatwell.example</span>
      <span>Website: marlatwell.example</span>
    </p>
  </section>
</body>
</html>
```